Personal Web page for recruiter and owner of consulting firm

I work full time as a recruiter so I want a page that allows for me to support my efforts. I would like a long single page, I need to be able to upload four two minute videos, and 4 images. I also want the color scheme to match with my consulting company. I own the domain marlowevantrees.com already through wordpress . I took a shot at it myself and its terrible.

Target Market(s)

Potential clients

Industry/Entity Type

Management Consulting

Logo Text

marlowe vantrees

Font styles to use
Serif

Requirements
Must have
• Must in color scheme go well with my consulting company logo attached
• Must be able to upload 4 two minute videos and 4 images (photos of me)
• Single long scroll page
• Modern and clean
Nice to have
• Easy for me to update videos images and text without complex coding
Should not have
• I want the design and feel to go well with my logos not exactly replicate it

```html
<!DOCTYPE html>
<html lang="en">
<head>
<meta charset="utf-8">
<title>Vantrees Strategies</title>
<link rel="stylesheet" href="https://fonts.googleapis.com/css2?family=Questrial&family=Lato:wght@400;700;900&family=Montserrat:wght@500;600&display=swap">
<style>
:root{
  --navy:#0b2b5e;
  --navy-deep:#072250;
  --ink:#2a2a2a;
  --text:#555;
  --muted:#9a9a9a;
  --line:#d8d8d8;
  --light:#f4f4f4;
  --white:#fff;
  --dark:#3a3a3a;
}
*{box-sizing:border-box;margin:0;padding:0}
html,body{width:1200px;height:4196px;overflow:hidden}
body{position:relative;background:var(--white);font-family:"Questrial",sans-serif;color:var(--text)}
.abs{position:absolute}

/* header */
.site-header{left:0;top:0;width:1200px;height:117px;background:var(--white)}
.brand{left:84px;top:44px;font-size:22px;letter-spacing:3px;color:var(--ink);white-space:nowrap;line-height:1}
.main-nav{left:518px;top:46px;display:flex;align-items:center;gap:22px;font-size:16px;color:var(--ink)}
.main-nav .active{background:var(--navy);color:var(--white);padding:4px 14px;border-radius:14px}
.nav-phone{display:flex;align-items:center;gap:10px;margin-left:26px}

/* hero */
.hero{left:0;top:117px;width:1200px;height:443px;background:linear-gradient(180deg,#3b3b3b,#555 55%,#2c2c2c)}
.hero-title{left:0;top:282px;width:1200px;text-align:center;color:var(--white);font-family:"Lato",sans-serif;font-weight:900;font-size:40px}
.hero-lead{left:360px;top:347px;width:480px;text-align:center;color:#eee;font-size:16px;line-height:1.5}

/* section titles */
.section-title{left:0;width:1200px;text-align:center;font-family:"Montserrat",sans-serif;font-weight:500;font-size:30px;letter-spacing:1px;color:var(--ink)}
.title-rule{left:450px;width:300px;height:2px;background:#bbb}
.title-rule::after{content:"";position:absolute;left:120px;top:-2px;width:60px;height:6px;border-radius:3px;background:var(--navy)}

.copy{font-size:13.5px;line-height:1.62;color:var(--text)}
.copy p+p{margin-top:18px}

.video{background:linear-gradient(135deg,#d9dcdf,#8b9399 60%,#4e555b)}
.video-bar{position:absolute;left:0;right:0;bottom:0;height:30px;background:rgba(0,0,0,.75)}
.video-top{position:absolute;left:0;right:0;top:0;height:22px;background:rgba(0,0,0,.55)}
.play{position:absolute;left:50%;top:50%;width:64px;height:44px;margin:-22px 0 0 -32px;background:#111;border-radius:10px}
.play::after{content:"";position:absolute;left:26px;top:12px;border-left:16px solid #fff;border-top:10px solid transparent;border-bottom:10px solid transparent}

/* services */
.service-card{height:223px;display:flex;background:var(--light)}
.service-card.raised{background:var(--white);box-shadow:0 2px 10px rgba(0,0,0,.18)}
.service-img{width:190px;height:100%}
.service-body{position:relative;flex:1;padding:36px 28px 0 44px}
.service-name{font-size:17px;font-weight:400;color:var(--navy);letter-spacing:.5px}
.service-card.plain .service-name{color:var(--ink)}
.service-text{margin-top:22px;font-size:13px;line-height:1.55}
.service-more{position:absolute;right:28px;bottom:38px;font-size:12px;color:var(--navy)}
.service-card.plain .service-more{color:#666}

/* stats */
.stats-band{left:0;top:1617px;width:1200px;height:361px;background:linear-gradient(90deg,#2e2e2e,#4a4a4a 50%,#2f2f2f)}
.stats-head{left:84px;top:1672px;color:var(--white);font-family:"Lato",sans-serif;font-weight:700;font-size:40px;line-height:1.2}
.stats-head small{font-size:33px;font-weight:700}
.stat{top:1830px;color:var(--white);font-family:"Lato",sans-serif}
.stat-num{font-size:42px;font-weight:900;line-height:1}
.stat-label{font-size:14px;margin-top:8px;letter-spacing:.3px}

/* news */
.news-band{left:0;top:2489px;width:1200px;height:568px;background:var(--light)}
.news-img{height:223px}
.news-title{font-size:19px;font-weight:400;color:var(--navy)}
.news-item.second .news-title{color:var(--ink)}
.news-date{font-size:12px;color:var(--muted);margin-top:6px}
.news-text{font-size:12.5px;color:#aaa;line-height:1.6;margin-top:6px}

/* contact */
.contact-item{width:300px;text-align:center;font-size:16px;color:var(--ink);line-height:1.9}
.contact-item svg{display:block;margin:0 auto 22px}
.field{font-size:11px;color:var(--ink);border-bottom:1px solid var(--line);padding-bottom:6px}
.send{left:565px;top:3739px;width:115px;height:40px;background:var(--dark);color:var(--white);font-size:14px;letter-spacing:1px;display:flex;align-items:center;justify-content:center}

/* footer */
.site-footer{left:0;top:3888px;width:1200px;height:308px;background:var(--navy-deep)}
.footer-brand{left:0;top:3966px;width:1200px;text-align:center;color:var(--white);font-size:30px;letter-spacing:4px;line-height:1}
.social{left:528px;top:4076px;display:flex;gap:24px}
.social span{width:20px;height:20px;background:var(--white);border-radius:3px}
.copyright{left:0;top:4145px;width:1200px;text-align:center;color:#cdd6e6;font-size:11px;letter-spacing:.5px}
</style>
</head>
<body>

<header class="abs site-header">
  <div class="abs brand">VANTREES STRATEGIES</div>
  <nav class="abs main-nav">
    <span class="active">HOME</span><span>ABOUT US</span><span style="margin-left:14px">SERVICES</span><span>NEWS</span><span>CONTACT US</span>
    <span class="nav-phone"><svg width="14" height="14" viewBox="0 0 24 24"><path fill="#2a2a2a" d="M6.6 10.8a15.1 15.1 0 0 0 6.6 6.6l2.2-2.2c.3-.3.7-.4 1-.2 1.1.4 2.3.6 3.6.6.6 0 1 .4 1 1V20c0 .6-.4 1-1 1A17 17 0 0 1 3 4c0-.6.4-1 1-1h3.5c.6 0 1 .4 1 1 0 1.3.2 2.5.6 3.6.1.3 0 .7-.2 1z"/></svg>0155 302 846</span>
  </nav>
</header>

<section class="abs hero" role="img" aria-label="Photo of business people in suits seated in a row, waiting for interviews"></section>
<h1 class="abs hero-title">WELCOME TO THE VANTREES</h1>
<p class="abs hero-lead">Lorem ipsum dolor sit amet consectetur labore magna aliqua elit sed do eiusmod tempor incididunt ut labore et.</p>

<h2 class="abs section-title" style="top:603px">ABOUT VANTREES</h2>
<div class="abs title-rule" style="top:668px"></div>
<div class="abs copy" style="left:84px;top:737px;width:505px">
  <p>There are many variations of passages of Lorem Ipsum available, but the majority have suffered alteration in some form, by injected humour, or randomised words which don't look even slightly believable. If you are going to use a passage of Lorem Ipsum, you need to be sure there isn't anything embarrassing hidden in the middle of text.</p>
  <p>All the Lorem Ipsum generators on the Internet tend to repeat predefined chunks as necessary, making this the first true generator on the Internet. It uses a dictionary of over 200 Latin words, combined with a handful of model sentence structures, to generate Lorem Ipsum which looks reasonable. The generated Lorem Ipsum is therefore always free from repetition, injected humour, or non-characteristic words etc.</p>
</div>
<div class="abs video" style="left:654px;top:733px;width:459px;height:279px" role="img" aria-label="Video still of a man in glasses speaking in an office">
  <div class="video-top"></div><div class="play"></div><div class="video-bar"></div>
</div>

<h2 class="abs section-title" style="top:1148px">SERVICES</h2>
<div class="abs title-rule" style="top:1208px"></div>
<article class="abs service-card raised" style="left:84px;top:1273px;width:492px">
  <div class="service-img" role="img" aria-label="Photo of a red dart hitting a target between running figures" style="background:linear-gradient(135deg,#eee,#b5b5b5 55%,#8a8a8a)"></div>
  <div class="service-body">
    <h3 class="service-name">RECRUITER</h3>
    <p class="service-text">Lorem ipsum dolor sit amet, consectetur adipiscing elit, sed do eiusmod tempor incididunt</p>
    <span class="service-more">LEARN MORE</span>
  </div>
</article>
<article class="abs service-card plain" style="left:627px;top:1273px;width:486px">
  <div class="service-img" role="img" aria-label="Photo of job candidates seated, one viewed through a magnifying glass" style="background:linear-gradient(135deg,#f2f2f2,#c9c4bd 55%,#8c8680)"></div>
  <div class="service-body">
    <h3 class="service-name">CONSULTING</h3>
    <p class="service-text">Lorem ipsum dolor sit amet, consectetur adipiscing elit, sed do eiusmod tempor incididunt</p>
    <span class="service-more">LEARN MORE</span>
  </div>
</article>

<section class="abs stats-band" role="img" aria-label="Dark photo of a dart hitting a target with running figures"></section>
<h2 class="abs stats-head">Doing the right thing,<br><small>at the right time.</small></h2>
<div class="abs stat" style="left:84px"><div class="stat-num">321</div><div class="stat-label">CASES COMPLETED</div></div>
<div class="abs stat" style="left:397px"><div class="stat-num">250</div><div class="stat-label">CONSULTANTS</div></div>
<div class="abs stat" style="left:677px"><div class="stat-num">150</div><div class="stat-label">AWARDS WINNING</div></div>
<div class="abs stat" style="left:962px"><div class="stat-num">100%</div><div class="stat-label">SATISFIED CUSTOMERS</div></div>

<h2 class="abs section-title" style="top:2018px">FUTURES SERVICES</h2>
<div class="abs title-rule" style="top:2078px"></div>
<div class="abs video" style="left:84px;top:2143px;width:459px;height:277px" role="img" aria-label="Video still of a man in glasses speaking in an office">
  <div class="video-top"></div><div class="play"></div><div class="video-bar"></div>
</div>
<div class="abs copy" style="left:593px;top:2143px;width:520px">
  <p>There are many variations of passages of Lorem Ipsum available, but the majority have suffered alteration in some form, by injected humour, or randomised words which don't look even slightly believable. If you are going to use a passage of Lorem Ipsum, you need to be sure there isn't anything embarrassing hidden in the middle of text.</p>
  <p>All the Lorem Ipsum generators on the Internet tend to repeat predefined chunks as necessary, making this the first true generator on the Internet. It uses a dictionary of over 200 Latin words, combined with a handful of model sentence structures, to generate Lorem Ipsum which looks reasonable. The generated Lorem Ipsum is therefore always free from repetition, injected humour, or non-characteristic words etc.</p>
</div>

<section class="abs news-band"></section>
<h2 class="abs section-title" style="top:2541px">NEWS</h2>
<div class="abs title-rule" style="top:2604px"></div>
<article class="abs news-item" style="left:84px;top:2652px;width:489px">
  <div class="news-img" role="img" aria-label="Photo of business people seated in a row of chairs" style="background:linear-gradient(180deg,#e9e9e9,#9a9a9a 55%,#5e5e5e)"></div>
  <h3 class="news-title" style="margin-top:20px">MarketingMedia &amp; Advertising</h3>
  <div class="news-date">Jan 26, 2017</div>
  <p class="news-text">Alias vero aspernatur libero vel, neque sequi non dignissimos ab architecto ratione perferendis, expedita quod quaerat dicta.</p>
</article>
<article class="abs news-item second" style="left:629px;top:2652px;width:487px">
  <div class="news-img" role="img" aria-label="Photo of a woman seated among empty white chairs" style="background:linear-gradient(180deg,#cfcfcf,#a7a7a7 60%,#8d8d8d)"></div>
  <h3 class="news-title" style="margin-top:20px">PlantFabrication and Erection</h3>
  <div class="news-date">Jan 26, 2017</div>
  <p class="news-text">Alias vero aspernatur libero vel, neque sequi non dignissimos ab architecto ratione perferendis, expedita quod quaerat dicta.</p>
</article>

<h2 class="abs section-title" style="top:3114px">CONTACT US</h2>
<div class="abs title-rule" style="top:3177px"></div>
<div class="abs contact-item" style="left:121px;top:3264px">
  <svg width="30" height="42" viewBox="0 0 24 34"><path fill="#0b2b5e" d="M12 0A12 12 0 0 0 0 12c0 9 12 22 12 22s12-13 12-22A12 12 0 0 0 12 0zm0 17a5 5 0 1 1 0-10 5 5 0 0 1 0 10z"/></svg>
  418 Alder Row, Millbrook,<br>Oregon, 97321.
</div>
<div class="abs contact-item" style="left:471px;top:3266px">
  <svg width="38" height="38" viewBox="0 0 24 24"><path fill="#0b2b5e" d="M6.6 10.8a15.1 15.1 0 0 0 6.6 6.6l2.2-2.2c.3-.3.7-.4 1-.2 1.1.4 2.3.6 3.6.6.6 0 1 .4 1 1V20c0 .6-.4 1-1 1A17 17 0 0 1 3 4c0-.6.4-1 1-1h3.5c.6 0 1 .4 1 1 0 1.3.2 2.5.6 3.6.1.3 0 .7-.2 1z"/></svg>
  0155 302 846
</div>
<div class="abs contact-item" style="left:807px;top:3270px">
  <svg width="44" height="34" viewBox="0 0 44 34"><rect width="44" height="34" rx="3" fill="#0b2b5e"/><path d="M3 5l19 15L41 5" stroke="#fff" stroke-width="3" fill="none"/></svg>
  info@marlowevantrees.com
</div>

<form class="abs" style="left:0;top:0">
  <div class="abs field" style="left:322px;top:3474px;width:601px">Name</div>
  <div class="abs field" style="left:322px;top:3569px;width:260px">Email</div>
  <div class="abs field" style="left:657px;top:3569px;width:266px">Phone</div>
  <div class="abs field" style="left:322px;top:3650px;width:601px">Message</div>
  <div class="abs send">SEND</div>
</form>

<footer class="abs site-footer"></footer>
<div class="abs footer-brand">VANTREES STRATEGIES</div>
<div class="abs social"><span></span><span></span><span></span><span></span></div>
<p class="abs copyright">VANTREES © 2017. ALL RIGHT RESERVED.</p>

</body>
</html>
```